Industrial automation company needs new business cards

We need a new business card designed. We have an existing logo that is very simple and are happy to consider changes to it. We have been in business for more than 10 years and our logo has some brand recognition.
We are a company of engineers and build systems for industrial automation, substation automation, power and energy monitoring and production data vertical integration. Our main clients are food manufacturers, data centers and government establishments.
Our current business cards have our name, qualifications, job title, telephone, email and web address details. We don't need our physical address on our business cards. I've attached our current logo

Industry/Entity Type

Business

Logo Text

vardo

Font styles to use
Sans Serif

Colors
6b449b

Requirements
Must have
• - double sided business cards
• - name (eg Mara Quill)
• - qualifications (BE Elec MAGSO)
• - job title (eg Senior Engineer)
• - telephone (eg 0472 518 396)
• - email (eg mara.quill@vardo.com.au)
• - web address (eg vardo.com.au)
Nice to have
• include our target markets on the back side of the card
• - industrial automation
• - substation automation
• - power and energy monitoring
• - production data vertical integration

```html
<!DOCTYPE html>
<html lang="en">
<head>
<meta charset="utf-8">
<title>Vardo Business Card</title>
<link rel="stylesheet" href="https://fonts.googleapis.com/css2?family=Open+Sans:wght@400;600;700&display=swap">
<style>
  :root {
    --backdrop: #2f2f2f;
    --brand-purple: #6b449b;
    --card-white: #f2f2f2;
    --text-grey: #3f3f3f;
    --rule-lilac: #9b86c4;
    --on-purple: #ffffff;
  }
  * { margin: 0; padding: 0; box-sizing: border-box; }
  html, body {
    width: 1200px;
    height: 900px;
    overflow: hidden;
    background: var(--backdrop);
    font-family: "Open Sans", Arial, sans-serif;
  }
  .stage {
    position: relative;
    width: 1200px;
    height: 900px;
  }
  .card {
    position: absolute;
    top: 170px;
    width: 347px;
    height: 561px;
    box-shadow: 2px 3px 6px rgba(0, 0, 0, 0.55);
  }
  .card-front {
    left: 259px;
    background: var(--card-white);
    text-align: center;
  }
  .card-back {
    left: 631px;
    background: var(--brand-purple);
  }
  .wordmark {
    position: absolute;
    left: 0;
    width: 100%;
    font-weight: 600;
    letter-spacing: 4px;
    line-height: 1;
  }
  .card-front .wordmark {
    top: 238px;
    font-size: 62px;
    color: var(--brand-purple);
  }
  .card-back .wordmark {
    top: 254px;
    font-size: 52px;
    color: var(--on-purple);
    text-align: center;
  }
  .holder {
    position: absolute;
    top: 362px;
    left: 0;
    width: 100%;
  }
  .holder-name {
    font-size: 19px;
    font-weight: 700;
    color: var(--brand-purple);
    line-height: 24px;
  }
  .holder-quals {
    font-size: 16px;
    font-weight: 400;
  }
  .holder-title {
    font-size: 15px;
    color: var(--text-grey);
    line-height: 20px;
  }
  .divider {
    position: absolute;
    top: 419px;
    left: 130px;
    width: 88px;
    height: 1px;
    background: var(--rule-lilac);
  }
  .contact-icons {
    position: absolute;
    top: 439px;
    left: 0;
    width: 100%;
    display: flex;
    justify-content: center;
    gap: 4px;
  }
  .contact-icons svg { width: 16px; height: 16px; }
  .contact-list {
    position: absolute;
    top: 459px;
    left: 0;
    width: 100%;
    list-style: none;
    font-size: 15px;
    line-height: 20.5px;
    color: var(--text-grey);
  }
</style>
</head>
<body>
<main class="stage">
  <section class="card card-front">
    <div class="wordmark">VARDO</div>
    <div class="holder">
      <p class="holder-name">MARA QUILL, <span class="holder-quals">BE Elec MAGSO</span></p>
      <p class="holder-title">Senior Engineer</p>
    </div>
    <div class="divider"></div>
    <div class="contact-icons" aria-hidden="true">
      <svg viewBox="0 0 16 16"><circle cx="8" cy="8" r="8" fill="#6b449b"/><path d="M4.5 6.2c0-1 .8-1.6 3.5-1.6s3.5.6 3.5 1.6l-1.3.3-.4-1.1H6.2l-.4 1.1z M5.5 7.2h5l.8 3.6H4.7z" fill="#fff"/></svg>
      <svg viewBox="0 0 16 16"><circle cx="8" cy="8" r="8" fill="#6b449b"/><rect x="4" y="5.2" width="8" height="5.6" fill="#fff"/><path d="M4 5.2l4 3 4-3" fill="none" stroke="#6b449b" stroke-width="0.8"/></svg>
      <svg viewBox="0 0 16 16"><circle cx="8" cy="8" r="8" fill="#6b449b"/><circle cx="8" cy="8" r="4" fill="none" stroke="#fff" stroke-width="1.2"/><path d="M4 8h8M8 4c-1.6 2.4-1.6 5.6 0 8M8 4c1.6 2.4 1.6 5.6 0 8" fill="none" stroke="#fff" stroke-width="0.9"/></svg>
    </div>
    <ul class="contact-list">
      <li>0472 518 396</li>
      <li>info@vardo.com.au</li>
      <li>www.vardo.com.au</li>
    </ul>
  </section>
  <section class="card card-back">
    <div class="wordmark">VARDO</div>
  </section>
</main>
</body>
</html>
```